Peach Point of Sale Cards for Grocery Retail Markets

We are looking to update our peach point of sale card and price card. The cards will need to be 7" x 11" with a .125 bleed - one sided. See attached for the old versions. We would like this to use photos that look like true Washington State Peaches. Here are the bullet points we would like to use: - New Crop!- Tree Ripened- Excellent FlavorNOTE: The price card just needs to have a space where a retailer can write in the sale price of the item. See attachment with the white box.

Target Market(s)

Retail market shoppers

Requirements
Must have
• Pictures of Peaches Only

```html
<!DOCTYPE html>
<html lang="en">
<head>
<meta charset="utf-8">
<title>Washington State Peaches – Point of Sale Card</title>
<link rel="stylesheet" href="https://fonts.googleapis.com/css2?family=Open+Sans:wght@700;800&family=Arimo:ital,wght@1,700&family=Yellowtail&display=swap">
<style>
  :root {
    --backdrop: #d9d9d9;
    --card: #ffffff;
    --brand-red: #a01d2b;
    --brand-green: #1f6b35;
    --green-shadow: #0c2a14;
    --band-red: #e8432a;
    --sun-yellow: #f2e52a;
    --peach-deep: #d9402a;
    --peach-light: #f08a3c;
    --leaf: #3f8a3a;
  }
  * { margin: 0; padding: 0; box-sizing: border-box; }
  html, body {
    width: 1200px; height: 1000px; overflow: hidden;
    background: var(--backdrop);
  }
  .pos-card {
    position: absolute; left: 348px; top: 103px;
    width: 504px; height: 793px;
    background: var(--card);
    overflow: hidden;
  }
  .corner-accents { position: absolute; inset: 0; }
  .headline {
    position: absolute; left: 60px; top: 26px;
    font-family: "Open Sans", sans-serif; font-weight: 800;
    font-size: 57px; letter-spacing: 0.5px; line-height: 1;
    color: var(--brand-red);
  }
  .subhead {
    position: absolute; right: 22px; top: 84px;
    font-family: "Open Sans", sans-serif; font-weight: 800;
    font-size: 39px; line-height: 1;
    color: var(--brand-green);
    text-shadow: 2px 3px 0 var(--green-shadow);
  }
  .product-photo {
    position: absolute; left: 16px; top: 118px;
    width: 478px; height: 398px;
    border-radius: 40% 45% 30% 35%;
    background:
      radial-gradient(ellipse 60% 55% at 55% 40%, var(--peach-light), var(--peach-deep) 70%, transparent 72%),
      radial-gradient(ellipse 70% 40% at 50% 75%, var(--leaf), transparent 70%);
  }
  .selling-points {
    position: absolute; left: 0; top: 0; list-style: none;
    font-family: "Arimo", sans-serif; font-style: italic; font-weight: 700;
    font-size: 26px; color: var(--brand-green);
    text-shadow: 0 0 3px #fff, 0 0 3px #fff;
  }
  .selling-points li { position: absolute; white-space: nowrap; }
  .point-new { left: 91px; top: 384px; }
  .point-ripe { left: 32px; top: 432px; }
  .point-flavor { left: 104px; top: 475px; }
  .price {
    position: absolute; left: 270px; top: 560px;
    font-family: "Open Sans", sans-serif; font-weight: 800;
    color: var(--brand-red); line-height: 1; white-space: nowrap;
  }
  .price-currency { font-size: 44px; vertical-align: top; position: relative; top: 4px; }
  .price-amount { font-size: 100px; letter-spacing: -2px; }
  .grower {
    position: absolute; left: 16px; top: 652px;
    display: flex; align-items: center; gap: 12px;
  }
  .grower-mark {
    width: 58px; height: 58px; border-radius: 50%;
    background: var(--peach-deep);
  }
  .grower-name {
    font-family: "Open Sans", sans-serif; font-weight: 700;
    font-size: 15px; line-height: 1.05; color: var(--brand-green);
  }
  .tagline-band {
    position: absolute; left: 0; bottom: 0;
    width: 100%; height: 65px;
    background: var(--band-red);
    display: flex; align-items: center; justify-content: center;
  }
  .tagline {
    font-family: "Yellowtail", cursive;
    font-size: 50px; color: #fff; letter-spacing: 1px;
    line-height: 1;
  }
</style>
</head>
<body>
  <article class="pos-card">
    <svg class="corner-accents" width="504" height="793" viewBox="0 0 504 793" aria-hidden="true">
      <path d="M-2 45 A 44 44 0 0 0 80 0" fill="none" stroke="var(--band-red)" stroke-width="6"/>
      <circle cx="34" cy="-4" r="40" fill="var(--sun-yellow)"/>
      <path d="M452 0 Q 470 48 504 72" fill="none" stroke="var(--band-red)" stroke-width="6"/>
    </svg>

    <h1 class="headline">WASHINGTON</h1>
    <h2 class="subhead">STATE PEACHES</h2>

    <div class="product-photo" role="img" aria-label="Photo of ripe red and orange peaches resting on green leaves"></div>

    <ul class="selling-points">
      <li class="point-new">NEW CROP!</li>
      <li class="point-ripe">TREE RIPENED</li>
      <li class="point-flavor">EXCELLENT FLAVOR</li>
    </ul>

    <p class="price"><span class="price-currency">$</span><span class="price-amount">99</span></p>

    <div class="grower">
      <span class="grower-mark" aria-hidden="true"></span>
      <p class="grower-name">Cascade Orchard<br>Growers</p>
    </div>

    <footer class="tagline-band">
      <p class="tagline">Taste The Difference</p>
    </footer>
  </article>
</body>
</html>
```